Brightmoor Leisure Works Investor Brochure

Start Up Company Brightmoor Leisure Works requires 4 page A4 size brochure outlining and detailing new product. Draft layout attached. Information and points of difference included. Company logo and graphics attached. Final design should sell to investors.
Industry/Entity Type
It Company

```html
<!DOCTYPE html>
<html lang="en">
<head>
<meta charset="utf-8">
<title>Brightmoor Leisure Works – Investor Brochure</title>
<link rel="stylesheet" href="https://fonts.googleapis.com/css2?family=Open+Sans:wght@300;400;600;700&family=Roboto+Condensed:wght@400;700&display=swap">
<style>
:root{
  --backdrop:#e7e4df;
  --paper:#ffffff;
  --blue:#2a8fd6;
  --blue-light:#5fb4ea;
  --blue-pale:#cfe6f6;
  --blue-deep:#1c6fae;
  --navy:#173a5c;
  --teal:#2f6f86;
  --ink:#333a40;
  --grey:#8a9096;
  --track:#e4e6e8;
  --charcoal:#3b3e42;
}
*{box-sizing:border-box;margin:0;padding:0}
html,body{width:1200px;height:899px;overflow:hidden;background:var(--backdrop)}
body{position:relative;font-family:"Open Sans",Arial,sans-serif;color:var(--ink)}
.page{position:absolute;top:188px;width:370px;height:523px;background:var(--paper);overflow:hidden;box-shadow:0 2px 8px rgba(0,0,0,.18)}
.cover{left:20px}
.spread-left{left:430px}
.spread-right{left:800px}
.spread-left::after{content:"";position:absolute;right:0;top:0;width:18px;height:100%;background:linear-gradient(to left,rgba(0,0,0,.08),transparent)}
.spread-right::before{content:"";position:absolute;left:0;top:0;width:18px;height:100%;background:linear-gradient(to right,rgba(0,0,0,.08),transparent);z-index:3}

/* cover */
.cover-photo{position:absolute;left:0;top:0;width:370px;height:170px;background:linear-gradient(160deg,#9aa6b2 0%,#c9d0d6 45%,#6f7d8a 100%);clip-path:polygon(0 0,100% 0,100% 62%,0 100%)}
.cover-band{position:absolute;left:0;top:0;width:370px;height:200px}
.kiosk{position:absolute;background:linear-gradient(180deg,#3e74c4,#1d3f86 70%,#122a5c)}
.cover .kiosk{left:38px;top:88px;width:56px;height:200px;border-radius:4px 4px 0 0}
.taglines{position:absolute;right:22px;top:196px;text-align:right;color:var(--blue);font-size:10.5px;line-height:20px;font-weight:400}
.table-title{position:absolute;left:22px;top:294px;font-size:8.5px;font-weight:700;color:var(--ink)}
.hosp-table{position:absolute;left:22px;top:308px;width:326px;border-collapse:collapse;font-family:"Roboto Condensed",Arial,sans-serif;font-size:6.5px}
.hosp-table th{background:var(--navy);color:#fff;font-weight:400;height:13px;padding:0 3px;text-align:center}
.hosp-table td{height:12px;padding:0 3px;text-align:center;background:var(--blue-pale);border-bottom:1px solid #fff}
.hosp-table td:first-child{text-align:left;width:112px}
.hosp-table tr.group td{background:var(--blue-deep);color:#fff;font-weight:700}
.hosp-table tr.total td{background:var(--blue);color:#fff}
.cover-foot{position:absolute;left:0;bottom:0;width:370px;height:62px;background:linear-gradient(180deg,var(--blue-light),var(--blue-deep));display:flex;align-items:center;justify-content:center;gap:8px}
.brand-mark{width:16px;height:16px;background:#fff}
.brand-name{color:#fff;font-size:13px;font-weight:700;letter-spacing:.5px}

/* spread left */
.headline{position:absolute;left:150px;top:24px;color:var(--grey)}
.headline .small{font-size:12px;font-weight:300;letter-spacing:.5px}
.headline .big{font-size:36px;font-weight:300;color:var(--blue);line-height:38px}
.aus-map{position:absolute;left:150px;top:82px;width:190px;height:160px;background:radial-gradient(ellipse at 50% 50%,var(--blue-light),var(--blue) 80%);border-radius:40% 50% 45% 40%}
.intro{position:absolute;left:22px;top:84px;width:118px;font-size:7px;line-height:10px;color:var(--ink)}
.intro p{margin-bottom:10px}
.passengers{position:absolute;left:22px;right:22px;top:258px;text-align:center;color:var(--blue);font-size:8.5px;line-height:11px}
.air-table{position:absolute;left:62px;top:290px;width:286px;border-collapse:collapse;font-family:"Roboto Condensed",Arial,sans-serif;font-size:7px;color:#fff}
.air-table caption{background:var(--navy);color:#fff;font-size:7.5px;text-align:left;padding:3px 6px}
.air-table td{height:15px;padding:0 6px}
.air-table td.city{text-align:right;width:26%}
.air-table tr:nth-child(odd) td{background:var(--blue)}
.air-table tr:nth-child(even) td{background:var(--teal)}
.spread-left .kiosk{left:14px;top:330px;width:48px;height:178px;border-radius:4px 4px 0 0;z-index:2}

/* spread right */
.world-map{position:absolute;left:26px;top:18px;width:330px;height:130px;background:radial-gradient(ellipse at 50% 50%,#5b5f64,#2f3236 85%);border-radius:30px}
.ribbon{position:absolute;left:0;top:50px;width:390px;height:28px;background:var(--charcoal);color:#fff;font-size:11px;letter-spacing:.5px;display:flex;align-items:center;justify-content:flex-end;padding-right:20px;transform:rotate(-6deg);transform-origin:left top;z-index:2}
.stat{position:absolute;left:22px;top:164px;font-size:8px;color:var(--grey)}
.section-title{position:absolute;left:22px;top:186px;font-size:15px;font-weight:300;color:var(--blue)}
.bars{position:absolute;left:26px;top:220px;display:flex;gap:10px;height:280px;align-items:flex-end}
.bar{position:relative;width:27px;height:100%;background:var(--track);border-radius:12px 12px 4px 4px;overflow:hidden}
.bar .fill{position:absolute;left:0;bottom:0;width:100%;background:var(--blue);display:flex;align-items:center;justify-content:center}
.bar .fill span{writing-mode:vertical-rl;transform:rotate(180deg);color:#fff;font-size:6.5px;line-height:8px;text-align:left;white-space:nowrap}
</style>
</head>
<body>

<section class="page cover">
  <div class="cover-photo" role="img" aria-label="Photograph of a modern glass office building under a cloudy sky"></div>
  <svg class="cover-band" viewBox="0 0 370 200" aria-hidden="true">
    <polygon points="0,170 370,105 370,118 0,186" fill="#2a8fd6"/>
    <polygon points="0,186 370,118 370,124 0,194" fill="#cfe6f6"/>
  </svg>
  <div class="kiosk" role="img" aria-label="Illustration of the blue movie rental kiosk"></div>
  <div class="taglines">
    <p>Movies for Travellers</p>
    <p>Download Movies in under 3 minutes</p>
    <p>No Internet Connection Required</p>
  </div>
  <p class="table-title">Public and Private Hospitals, States and Territories, 2012-13</p>
  <table class="hosp-table">
    <tr><th></th><th>NSW</th><th>Vic</th><th>Qld</th><th>WA</th><th>SA</th><th>Tas</th><th>ACT</th><th>NT</th><th>Total</th></tr>
    <tr class="group"><td colspan="10">PUBLIC HOSPITALS</td></tr>
    <tr><td>Public acute hospitals</td><td>218</td><td>149</td><td>166</td><td>88</td><td>78</td><td>22</td><td>3</td><td>5</td><td>729</td></tr>
    <tr><td>Public psychiatric hospitals</td><td>7</td><td>1</td><td>4</td><td>2</td><td>2</td><td>1</td><td>–</td><td>–</td><td>17</td></tr>
    <tr class="total"><td>Total public hospitals</td><td>225</td><td>150</td><td>170</td><td>90</td><td>80</td><td>23</td><td>3</td><td>5</td><td>746</td></tr>
    <tr class="group"><td colspan="10">PRIVATE HOSPITALS</td></tr>
    <tr><td>Private free-standing day</td><td>96</td><td>85</td><td>52</td><td>25</td><td>26</td><td>0</td><td>0</td><td>0</td><td>311</td></tr>
    <tr><td>Other private hospitals</td><td>89</td><td>79</td><td>53</td><td>32</td><td>28</td><td>0</td><td>0</td><td>0</td><td>281</td></tr>
    <tr class="total"><td>Total private hospitals</td><td>185</td><td>164</td><td>105</td><td>57</td><td>54</td><td>0</td><td>0</td><td>0</td><td>592</td></tr>
    <tr class="total"><td>All hospitals</td><td>410</td><td>314</td><td>275</td><td>147</td><td>134</td><td>23</td><td>3</td><td>5</td><td>1,338</td></tr>
  </table>
  <footer class="cover-foot">
    <span class="brand-mark"></span>
    <span class="brand-name">BRIGHTMOOR LEISURE WORKS</span>
  </footer>
</section>

<section class="page spread-left">
  <div class="headline">
    <p class="small">AIRPORTS ACROSS</p>
    <p class="big">AUSTRALIA</p>
  </div>
  <div class="aus-map" role="img" aria-label="Map of Australia marking airport locations"></div>
  <div class="intro">
    <p>Kiosks hold up to 400 new release movies to choose from.</p>
    <p>Travellers can browse and rent titles using FREE Wifi.</p>
    <p>Passengers are always killing time before and between flights. Perfect for new release movies. Target of 1 million transactions in the first 12 months.</p>
  </div>
  <p class="passengers">145,000,000+ Passenger Movements for YE Feb 2014. Up 3.1% on 2013</p>
  <div class="kiosk" role="img" aria-label="Illustration of the blue movie rental kiosk"></div>
  <table class="air-table">
    <caption>New Airport announced for Western Sydney to cope with increase demand.</caption>
    <tr><td class="city">SYDNEY</td><td>38 457 737</td><td class="city">MELBOURNE</td><td>30 484 074</td></tr>
    <tr><td class="city">BRISBANE</td><td>21 570 625</td><td class="city">PERTH</td><td>12 989 955</td></tr>
    <tr><td class="city">ADELAIDE</td><td>7 460 471</td><td class="city">GOLD COAST</td><td>5 789 386</td></tr>
    <tr><td class="city">CAIRNS</td><td>4 295 485</td><td class="city">CANBERRA</td><td>2 951 006</td></tr>
    <tr><td class="city">HOBART</td><td>2 098 416</td><td class="city">DARWIN</td><td>2 023 665</td></tr>
    <tr><td class="city">TOWNSVILLE</td><td>1 543 457</td><td class="city">LAUNCESTON</td><td>1 287 599</td></tr>
    <tr><td class="city">WILLIAMTOWN</td><td>1 208 188</td><td class="city">MACKAY</td><td>1 093 805</td></tr>
    <tr><td class="city">SUNSHINE COAST</td><td>891 300</td><td class="city">KARRATHA</td><td>763 537</td></tr>
    <tr><td class="city">ROCKHAMPTON</td><td>694 368</td><td class="city">ALICE SPRINGS</td><td>667 363</td></tr>
    <tr><td class="city">GLADSTONE</td><td>500 429</td><td class="city">PORT HEDLAND</td><td>491 274</td></tr>
  </table>
</section>

<section class="page spread-right">
  <div class="world-map" role="img" aria-label="Dark grey world map"></div>
  <div class="ribbon">TECHNOLOGY BUILT FOR GLOBAL EXPANSION</div>
  <p class="stat">Top-20 Airports in the world exceeded 1.2 billion passengers in 2013</p>
  <h2 class="section-title">Incorporating Blazing Fast Wifi</h2>
  <div class="bars">
    <div class="bar"><div class="fill" style="height:100%"><span>WiGig 802.11ad (7Gbps)<br>Future Device to Download SD Movies in 4 seconds</span></div></div>
    <div class="bar"><div class="fill" style="height:86%"><span>Wifi 802.11ac (1300 Mbps)<br>Orbit Phone X4 &amp; X5</span></div></div>
    <div class="bar"><div class="fill" style="height:72%"><span>Wifi 802.11n (300 Mbps)<br>5S Model Lumo Phone – Download SD Movie in under 3 minutes</span></div></div>
    <div class="bar"><div class="fill" style="height:30%"><span>Wifi 802.11g<br>(108 Mbps)</span></div></div>
    <div class="bar"><div class="fill" style="height:28%"><span>NetLink 100<br>(100 Mbps)</span></div></div>
    <div class="bar"><div class="fill" style="height:24%"><span>NetLink 50<br>(50 Mbps)</span></div></div>
    <div class="bar"><div class="fill" style="height:20%"><span>NetLink 25<br>(25Mbps)</span></div></div>
    <div class="bar"><div class="fill" style="height:18%"><span>NetLink 12<br>(12Mbps)</span></div></div>
    <div class="bar"><div class="fill" style="height:16%"><span>ADSL 2+<br>(24Mbps)</span></div></div>
  </div>
</section>

</body>
</html>
```